Business Card Design

We are a law firm which provides services to creditors.....we do collection litigation. I am wide open on suggestions. I was thinking of a square card? Alternatively, a vertically oriented standard card or a folded card.....something unique. I would like to use my firm logo and beyond that, I am open for any and all suggestions. I'm uncertain if the complete log is uploaded? If not, please let me email it to you.

Industry/Entity Type

Law Firm

Contact Information for Business Card

Harte, Quill & Dorsey, P.C.
Tom Dorsey, Lawyer
4187 W Cobbler Ave
Oklahoma City, OK 73116
tdorsey@HqdLegal.com
www.HqdLegal.com
mobile: 405-555-0182

```html
<!DOCTYPE html>
<html lang="en">
<head>
<meta charset="utf-8">
<title>Harte, Quill &amp; Dorsey, P.C. — Business Card</title>
<link rel="stylesheet" href="https://fonts.googleapis.com/css2?family=Open+Sans:wght@400;600;700&family=Questrial&display=swap">
<style>
  :root {
    --stage: #6a5034;
    --gold-light: #cdb73c;
    --gold-mid: #b8892a;
    --brown-deep: #93611c;
    --green: #1f8c5c;
    --green-dark: #146a44;
    --title-gold: #e7c24a;
    --ink-light: #ffffff;
    --ink-soft: #fbf3da;
  }
  * { box-sizing: border-box; margin: 0; padding: 0; }
  html, body {
    width: 1200px; height: 900px; overflow: hidden;
    background: var(--stage);
  }
  .canvas {
    width: 1200px; height: 900px;
    display: flex; align-items: center; justify-content: center; gap: 90px;
  }
  .card {
    position: relative;
    width: 380px; height: 664px;
    border-radius: 4px;
    overflow: hidden;
    box-shadow: 0 14px 34px rgba(0,0,0,.35);
    font-family: "Open Sans", sans-serif;
  }
  .card--front {
    background: linear-gradient(160deg, var(--gold-light) 0%, var(--gold-mid) 45%, var(--brown-deep) 100%);
  }
  .card--back {
    background: linear-gradient(165deg, var(--gold-light) 0%, #c49e30 50%, var(--gold-mid) 100%);
  }
  .firm-mark {
    position: absolute; left: 0; right: 0;
    display: flex; flex-direction: column; align-items: center; gap: 14px;
  }
  .card--front .firm-mark { top: 70px; }
  .card--back .firm-mark { top: 200px; }
  .firm-mark__dot {
    width: 86px; height: 86px; border-radius: 50%;
    background: var(--green);
  }
  .firm-mark__name {
    font-weight: 700; font-size: 19px; color: var(--ink-light);
    text-align: center; letter-spacing: .3px;
  }
  .contact {
    position: absolute; left: 0; right: 0; top: 330px;
    text-align: center; color: var(--ink-soft);
  }
  .contact__name {
    font-weight: 700; font-size: 30px; color: var(--ink-light);
  }
  .contact__title {
    font-weight: 600; font-size: 16px; color: var(--title-gold);
    margin: 2px 0 26px;
  }
  .contact__line { font-size: 16px; line-height: 1.45; }
  .contact__gap { height: 14px; }
  .web-band {
    position: absolute; left: 0; right: 0; bottom: 0; height: 62px;
    background: linear-gradient(180deg, var(--green) 0%, var(--green-dark) 100%);
    display: flex; align-items: center; justify-content: center;
    color: var(--ink-light); font-size: 18px; letter-spacing: 1.5px; font-weight: 600;
  }
  .back-web {
    position: absolute; right: 34px; bottom: 40px;
    font-family: "Questrial", sans-serif; font-size: 20px;
    color: var(--ink-light); letter-spacing: 1px;
  }
</style>
</head>
<body>
  <main class="canvas">
    <section class="card card--front" aria-label="Card front">
      <div class="firm-mark">
        <span class="firm-mark__dot"></span>
        <span class="firm-mark__name">Harte, Quill &amp; Dorsey, P.C.</span>
      </div>
      <div class="contact">
        <h1 class="contact__name">P.C. Tom Dorsey</h1>
        <p class="contact__title">Lawyer</p>
        <p class="contact__line">4187 W Cobbler Ave Norman</p>
        <p class="contact__line">OK 73069</p>
        <div class="contact__gap"></div>
        <p class="contact__line">Email: tdorsey@HqdLegal.com</p>
        <p class="contact__line">mobile: 405-555-0182</p>
      </div>
      <div class="web-band">WWW.HQDLEGAL.COM</div>
    </section>

    <section class="card card--back" aria-label="Card back">
      <div class="firm-mark">
        <span class="firm-mark__dot"></span>
        <span class="firm-mark__name">Harte, Quill &amp; Dorsey, P.C.</span>
      </div>
      <p class="back-web">www.HqdLegal.com</p>
    </section>
  </main>
</body>
</html>
```